R. Dalworth Billboard

2 miles ahead on right
Voted number 1 ... again!
California cuisine
Located in Historic Bramble Hollow Inn
Picture of a couple dining
www.marduvel.com 555.317.0962

Target Market(s)

travelers

Industry/Entity Type

hospitality

Font styles to use
Serif

Colors
59FF00
82FF00
B8FF75
E3FFCB
F4FFEA
EE7325
F08F49
F5BC92
FAE3D3
FDF4ED

Requirements
Should not have
• bright colors

```html
<!DOCTYPE html>
<html lang="en">
<head>
<meta charset="utf-8">
<title>R. Dalworth Billboard</title>
<link rel="stylesheet" href="https://fonts.googleapis.com/css2?family=Caladea&family=Libre+Baskerville:wght@400;700&family=Playfair+Display:wght@700&display=swap">
<style>
  :root {
    --wine: #8a100e;
    --gold: #f5ad16;
    --ribbon-shadow: #d9920c;
    --cream: #ffffff;
    --photo-dark: #3a1c08;
    --photo-mid: #b5581c;
    --photo-warm: #e0832e;
  }
  * { margin: 0; padding: 0; box-sizing: border-box; }
  html, body { width: 1200px; height: 500px; overflow: hidden; background: var(--wine); }
  .billboard {
    position: relative;
    width: 1200px;
    height: 500px;
    background: var(--wine);
    font-family: "Caladea", Cambria, Georgia, serif;
    overflow: hidden;
  }
  .dining-photo {
    position: absolute;
    left: 0; top: 0;
    width: 559px; height: 500px;
    background:
      radial-gradient(ellipse at 70% 45%, var(--photo-warm) 0%, transparent 55%),
      radial-gradient(ellipse at 30% 80%, var(--photo-mid) 0%, transparent 60%),
      linear-gradient(160deg, var(--photo-dark) 0%, #6b3410 55%, #9a4a16 100%);
  }
  .headline {
    position: absolute;
    left: 144px; top: 36px;
    font-family: "Playfair Display", Georgia, serif;
    font-weight: 700;
    font-size: 74px;
    line-height: 1;
    letter-spacing: 1.5px;
    color: var(--cream);
    white-space: nowrap;
  }
  .ribbon-tail {
    position: absolute;
    left: 637px; top: 161px;
    width: 50px; height: 58px;
  }
  .ribbon {
    position: absolute;
    left: 679px; top: 146px;
    width: 521px; height: 59px;
    background: var(--gold);
  }
  .ribbon-text {
    position: absolute;
    top: 151px;
    font-size: 44px;
    line-height: 1;
    color: var(--wine);
    white-space: nowrap;
  }
  .ribbon-text.voted { left: 687px; }
  .ribbon-text.again { left: 1028px; }
  .rank {
    position: absolute;
    left: 945px; top: 100px;
    width: 90px; height: 150px;
    overflow: visible;
    filter: drop-shadow(2px 3px 3px rgba(0,0,0,0.3));
  }
  .rank text {
    font-family: "Libre Baskerville", Georgia, serif;
    font-weight: 400;
    font-size: 162px;
    fill: var(--cream);
  }
  .brand-box {
    position: absolute;
    left: 644px; top: 353px;
    width: 139px; height: 70px;
    background: var(--cream);
    display: flex;
    flex-direction: column;
    align-items: center;
    justify-content: center;
    color: var(--wine);
    font-family: "Libre Baskerville", Georgia, serif;
    font-weight: 700;
    text-align: center;
  }
  .brand-name { font-size: 17px; line-height: 1.1; }
  .brand-sub { font-size: 8px; letter-spacing: 1px; line-height: 1.3; }
  .location {
    position: absolute;
    left: 797px; top: 364px;
    font-size: 19px;
    line-height: 25px;
    letter-spacing: 1px;
    color: var(--cream);
    text-transform: uppercase;
    white-space: nowrap;
  }
  .contact {
    position: absolute;
    left: 644px; top: 434px;
    display: flex;
    gap: 12px;
    font-size: 31px;
    line-height: 1;
    color: var(--cream);
    white-space: nowrap;
  }
  .cuisine {
    position: absolute;
    left: 82px; top: 441px;
    font-family: "Libre Baskerville", Georgia, serif;
    font-weight: 700;
    font-size: 26px;
    letter-spacing: 3px;
    line-height: 1;
    color: var(--cream);
    text-transform: uppercase;
    white-space: nowrap;
  }
</style>
</head>
<body>
<main class="billboard">
  <div class="dining-photo" role="img" aria-label="A couple dining together with a large burger, fries and a glass of beer in warm light"></div>

  <h1 class="headline">2 MILES AHEAD ON RIGHT</h1>

  <svg class="ribbon-tail" viewBox="0 0 50 58" aria-hidden="true">
    <polygon points="0,0 50,0 50,58 0,58 18,29" fill="var(--gold)"/>
    <polygon points="42,0 50,0 50,58 42,58" fill="var(--ribbon-shadow)"/>
  </svg>
  <div class="ribbon"></div>
  <span class="ribbon-text voted">Voted Number</span>
  <svg class="rank" viewBox="0 0 90 150" aria-label="1">
    <text x="45" y="140" text-anchor="middle">1</text>
  </svg>
  <span class="ribbon-text again">AGAIN!</span>

  <div class="brand-box">
    <span class="brand-name">Marduvel's</span>
    <span class="brand-sub">SOUTHWEST</span>
    <span class="brand-sub">BAR &amp; GRILL</span>
  </div>

  <p class="location">Located in<br>Historic Bramble Hollow Inn</p>

  <p class="contact">
    <span class="web">www.marduvel.com</span>
    <span class="phone">555.317.0962</span>
  </p>

  <p class="cuisine">California Cuisine</p>
</main>
</body>
</html>
```